engineering and fabrication company- KelbroTek

We require a full functional and coded website design for an engineering and fabrication company in Western Australia.
I have attached capability statement with a content of this website.
I would like to have Fabrication services divided into two sections

1. Steel Fabrication
2. Plastic Fabrication

Industry/Entity Type

mining , waste water , oil and gas , engineering and design

Coding

Coded - Design and coding required

Number of Pages Required

5+ page

Colors
0054AA
0677BA
7BADD7
CADEEF
E8F1F8
0094D4
00A9DD
6FCCEA
C7EBF8
E9F6FB

Requirements
Must have
• Must look very professional

```html
<!DOCTYPE html>
<html lang="en">
<head>
<meta charset="utf-8">
<title>KelbroTek — Engineering and Fabrication Work</title>
<link href="https://fonts.googleapis.com/css2?family=Raleway:wght@400;500;600;700&family=Montserrat:wght@800&family=Lato:wght@400;700&display=swap" rel="stylesheet">
<style>
:root{
  --blue:#1477dc;
  --blue-deep:#0054aa;
  --blue-sky:#1d9be6;
  --blue-band:#0e6fd8;
  --ink:#1d1d1d;
  --text:#444;
  --muted:#666;
  --dark:#15181d;
  --footer:#1b1b1b;
  --white:#fff;
  --line:#9a9a9a;
}
*{box-sizing:border-box;margin:0;padding:0}
html,body{width:1200px;height:4234px;overflow:hidden}
body{position:relative;font-family:"Lato",sans-serif;color:var(--text);background:var(--white)}
.abs{position:absolute}
.h{font-family:"Raleway",sans-serif}
.btn{position:absolute;background:var(--blue);color:var(--white);font:700 11px "Raleway",sans-serif;letter-spacing:.3px;display:flex;align-items:center;justify-content:center;text-transform:uppercase}
.ph{position:absolute}

/* top bar + hero */
.topbar{left:0;top:0;width:1200px;height:23px;background:#141414;z-index:3;color:#ddd;font-size:11px}
.topbar .social{left:130px;top:7px;display:flex;gap:22px}
.topbar .dot{width:9px;height:9px;border-radius:50%;background:#ddd}
.topbar .contact{right:130px;top:4px;display:flex;gap:22px;align-items:center}
.topbar svg{vertical-align:-2px;margin-right:4px}
.hero{left:0;top:0;width:1200px;height:534px;background:radial-gradient(ellipse at 78% 45%,#3a4f6a 0%,#1d2733 40%,#0c1118 100%)}
.logo{left:131px;top:30px;color:var(--white);z-index:3}
.logo .name{font:700 22px "Raleway",sans-serif;letter-spacing:.5px}
.logo .tag{font-size:6px;color:#cfe3f7;margin-top:1px}
.nav{top:38px;right:130px;display:flex;gap:14px;z-index:3}
.nav a{color:#e8eef5;font:500 11px "Raleway",sans-serif;text-decoration:none;padding:6px 12px}
.nav a.active{border:1px solid var(--white)}
.hero-kicker{left:0;width:1200px;top:145px;text-align:center;color:var(--white);font:500 26px "Raleway",sans-serif}
.hero-title{left:0;width:1200px;top:192px;text-align:center;color:var(--white);font:800 68px/1.02 "Montserrat",sans-serif;letter-spacing:.5px}
.slide-no{left:131px;top:477px;width:157px;height:57px;background:var(--blue-band);color:var(--white);font:500 17px "Raleway",sans-serif;padding:18px 0 0 16px}
.slide-no small{font-size:10px;margin-left:3px}
.slide-bar{left:236px;top:504px;width:84px;height:2px;background:var(--white)}
.slide-track{left:320px;top:504px;width:880px;height:1px;background:rgba(255,255,255,.35)}

/* company */
.eyebrow{font:500 10px "Raleway",sans-serif;color:var(--ink);text-transform:uppercase}
.title-lg{font:500 34px/1.2 "Raleway",sans-serif;color:var(--ink)}
.body-sm{font-size:11.5px;line-height:19px;color:var(--text)}

/* commitment */
.commit{left:0;top:1003px;width:1200px;height:505px;background:radial-gradient(ellipse at 55% 55%,#2c3440 0%,#1a1f26 55%,#101318 100%)}
.commit-title{left:0;width:1200px;top:1050px;text-align:center;color:var(--white);font:500 33px "Raleway",sans-serif}
.commit-sub{left:0;width:1200px;top:1093px;text-align:center;color:#cfd3d8;font-size:12px}
.card{top:1156px;height:297px;background:rgba(40,44,50,.85);text-align:center;color:var(--white)}
.card svg{margin-top:52px}
.card h3{font:600 18px "Raleway",sans-serif;margin-top:20px;letter-spacing:.3px}
.card p{font-size:10.5px;line-height:17px;color:#d6d6d6;margin:14px 36px 0}

/* services */
.svc-band{left:0;top:1508px;width:1200px;height:342px;background:linear-gradient(90deg,#0d6fd9,#0b63cc)}
.svc-title{left:0;width:1200px;text-align:center;color:var(--white)}
.svc-card-title{text-align:center;font:500 19px "Raleway",sans-serif;color:var(--ink)}
.svc-card-text{text-align:center;font-size:11.5px;line-height:19px;color:var(--text)}

/* split sections */
.sky{background:var(--blue-sky)}
.tank{background:linear-gradient(180deg,#e4e7ec,#b9bec7)}

/* mission */
.mission{left:0;top:2994px;width:1200px;height:429px;background:linear-gradient(90deg,#1e3d63 0%,#15263b 35%,#0d1521 60%,#090d14 100%)}

/* contact */
.field{height:24px;border-bottom:1px solid var(--line);font-size:9.5px;color:#333;padding-top:4px}
.msg{left:283px;top:3666px;width:634px;height:74px;border:1px solid var(--line);font-size:9.5px;color:#333;padding:12px}

/* footer */
.footer{left:0;top:3850px;width:1200px;height:384px;background:var(--footer);color:#ddd}
.f-head{color:var(--blue-sky);font:500 16px "Raleway",sans-serif}
.f-links{font-size:10.5px;line-height:26.5px;color:#e5e5e5}
.f-item{display:flex;align-items:flex-start;gap:9px;font-size:10px;line-height:14px;color:#e5e5e5}
.f-icon{width:27px;height:27px;border-radius:50%;border:1px solid #ddd;display:flex;align-items:center;justify-content:center;flex:none}
.gal{width:64px;height:49px}
.soc{width:32px;height:32px;border-radius:50%;background:var(--blue-sky)}
</style>
</head>
<body>

<!-- hero -->
<div class="abs hero ph" role="img" aria-label="Welder in protective mask working on steel in a dark workshop"></div>
<div class="abs topbar">
  <div class="abs social"><span class="dot"></span><span class="dot"></span><span class="dot"></span></div>
  <div class="abs contact">
    <span><svg width="9" height="10" viewBox="0 0 24 24"><path fill="#ddd" d="M6.6 10.8a15 15 0 0 0 6.6 6.6l2.2-2.2c.3-.3.7-.4 1-.2 1.1.4 2.3.6 3.6.6.6 0 1 .4 1 1V20c0 .6-.4 1-1 1A17 17 0 0 1 3 4c0-.6.4-1 1-1h3.5c.6 0 1 .4 1 1 0 1.3.2 2.5.6 3.6.1.3 0 .7-.2 1z"/></svg>+2 (555) 407 3921</span>
    <span><svg width="11" height="9" viewBox="0 0 24 18"><rect width="24" height="18" rx="2" fill="#ddd"/><path d="M1 2l11 8 11-8" stroke="#141414" stroke-width="2" fill="none"/></svg>info@kelbrotek.com</span>
  </div>
</div>
<div class="abs logo"><div class="name">KelbroTek</div><div class="tag">Design / Engineering / Fabrication</div></div>
<nav class="abs nav">
  <a class="active">HOME</a><a>ABOUT US</a><a>SERVICES</a><a>COMPANY</a><a>CONTACT US</a>
</nav>
<div class="abs hero-kicker">WESTERN AUSTRALIA</div>
<h1 class="abs hero-title">ENGINEERING AND<br>FABRICATION WORK</h1>
<div class="btn" style="left:529px;top:362px;width:142px;height:41px">Discover More</div>
<div class="abs slide-no">01/<small>03</small></div>
<div class="abs slide-track"></div>
<div class="abs slide-bar"></div>

<!-- company -->
<div class="ph" style="left:131px;top:534px;width:398px;height:406px;background:linear-gradient(160deg,#8d97a3,#4a535e 60%,#2c333b)" role="img" aria-label="Industrial steel pipework with valves and gauges"></div>
<div class="abs eyebrow" style="left:608px;top:576px">Our Company</div>
<div class="abs title-lg" style="left:608px;top:594px">Engineering and<br>Fabrication</div>
<p class="abs body-sm" style="left:610px;top:694px;width:464px">The guiding force in all that we do is our commitment to providing hands-on reliable customer service and quality metal and plastic components for a broad range of industries including Mining, Chemical Industry, Oil and Gas , Water Treatment, Agricultural Equipment, Material Handling, Construction Equipment, Renewable Energy &amp; more.</p>
<p class="abs body-sm" style="left:610px;top:782px;width:464px">At our Bayridge location, you will find a team of experienced manufacturing professionals ready to provide value-added services including integrated project management, new product development...</p>
<div class="btn" style="left:609px;top:861px;width:108px;height:35px">Read More</div>

<!-- commitment -->
<div class="abs commit ph" role="img" aria-label="Dark workshop with sparks from metal grinding"></div>
<h2 class="abs commit-title">Our Commitment</h2>
<div class="abs commit-sub">With every job we take on, KelbroTek promises to deliver</div>

<div class="abs card" style="left:131px;width:298px">
  <svg width="76" height="70" viewBox="0 0 76 70"><path d="M38 2l30 11v20c0 17-13 29-30 35C21 62 8 50 8 33V13z" fill="#1e88e5"/><circle cx="38" cy="34" r="15" fill="none" stroke="#fff" stroke-width="3"/><path d="M31 34l5 5 9-10" fill="none" stroke="#fff" stroke-width="3"/></svg>
  <h3>QUALITY</h3>
  <p>We understand the level of precision required to seamlessly carry out fabrication projects, so our processes are designed to guarantee the highest level of quality on every job.</p>
</div>
<div class="abs card" style="left:450px;width:300px">
  <svg width="76" height="70" viewBox="0 0 76 70"><path d="M38 2l30 11v20c0 17-13 29-30 35C21 62 8 50 8 33V13z" fill="#1e88e5"/><rect x="26" y="22" width="24" height="24" rx="3" fill="none" stroke="#fff" stroke-width="3"/><path d="M30 42l14-14" stroke="#fff" stroke-width="3"/></svg>
  <h3>TRANSPARENCY</h3>
  <p>From initial budget estimates to the end of construction, our team is dedicated to transparency throughout the entire process, so you always know where your project stands.</p>
</div>
<div class="abs card" style="left:771px;width:299px">
  <svg width="76" height="70" viewBox="0 0 76 70"><path d="M38 2l30 11v20c0 17-13 29-30 35C21 62 8 50 8 33V13z" fill="#1e88e5"/><circle cx="38" cy="28" r="8" fill="none" stroke="#fff" stroke-width="3"/><path d="M20 40c5 0 8 6 18 6s13-6 18-6" fill="none" stroke="#fff" stroke-width="3"/></svg>
  <h3>SUPPORT</h3>
  <p>A dedicated project team, including some of our top executives, will guide you through your project. When you have questions or concerns, we're right by your side.</p>
</div>

<!-- services -->
<div class="abs svc-band"></div>
<div class="abs svc-title" style="top:1549px;font:500 10px 'Raleway',sans-serif">WHAT WE OFFER</div>
<div class="abs svc-title h" style="top:1568px;font:600 33px 'Raleway',sans-serif">Our Services</div>
<div class="abs svc-title" style="top:1622px;font-size:11.5px;line-height:19px;color:#dbe9fb">KelbroTek operates steel and plastic fabrication facilities, utilizing the latest high-tech machinery and cutting-edge computer-driven processes<br>to bring the pieces you need to life with the precision you rely on.</div>

<div class="ph" style="left:131px;top:1702px;width:459px;height:287px;background:linear-gradient(150deg,#c2c8cf,#7b848f 55%,#3d454f)" role="img" aria-label="Stainless steel pipe assembly in a fabrication plant"></div>
<div class="ph" style="left:610px;top:1702px;width:460px;height:287px;background:linear-gradient(160deg,#5a5f66,#2f3339 50%,#8a6a44)" role="img" aria-label="Stacks of black plastic sheet parts on wooden pallets"></div>
<div class="abs svc-card-title" style="left:131px;width:459px;top:2007px">STEEL FABRICATION</div>
<div class="abs svc-card-title" style="left:610px;width:460px;top:2007px">PLASTIC FABRICATION</div>
<p class="abs svc-card-text" style="left:170px;width:381px;top:2046px">KelbroTek steel division manufactures in house a vast array of steel pipe components...</p>
<p class="abs svc-card-text" style="left:650px;width:380px;top:2046px">KelbroTek manufactures a range of pipe spools to customer's requirements.</p>
<div class="btn" style="left:306px;top:2103px;width:108px;height:36px">Read More</div>
<div class="btn" style="left:786px;top:2103px;width:108px;height:36px">Read More</div>

<!-- computer aided design -->
<div class="abs sky" style="left:0;top:2200px;width:529px;height:398px"></div>
<div class="ph tank" style="left:0;top:2269px;width:112px;height:259px" role="img" aria-label="3D model of a steel access stair"></div>
<div class="ph tank" style="left:131px;top:2269px;width:219px;height:259px" role="img" aria-label="3D model of a cylindrical storage tank"></div>
<div class="ph tank" style="left:372px;top:2269px;width:220px;height:259px" role="img" aria-label="3D model of a rectangular tank with hatches"></div>
<div class="abs title-lg" style="left:608px;top:2286px">Computer Aided Design</div>
<p class="abs" style="left:610px;top:2352px;width:470px;font-size:13.5px;line-height:21px;color:#222">From beginning to end, KelbroTek provides unbeatable engineering support to ensure every project is a success.</p>
<p class="abs body-sm" style="left:610px;top:2406px;width:440px">One of the services that KelbroTek offers its customers is its ability to provide extensive 3D Computer Aided Design.</p>
<div class="btn" style="left:609px;top:2469px;width:108px;height:35px">Read More</div>

<!-- storage tanks -->
<div class="abs sky" style="left:672px;top:2598px;width:528px;height:396px"></div>
<div class="ph tank" style="left:612px;top:2667px;width:220px;height:259px" role="img" aria-label="3D model of an open tank with mixer"></div>
<div class="ph tank" style="left:852px;top:2667px;width:220px;height:259px" role="img" aria-label="3D model of a cylindrical storage tank"></div>
<div class="ph tank" style="left:1092px;top:2667px;width:108px;height:259px" role="img" aria-label="3D model of a rectangular tank"></div>
<div class="abs title-lg" style="left:129px;top:2669px">Industrial Storage and<br>Process Tanks</div>
<p class="abs body-sm" style="left:131px;top:2766px;width:420px">KelbroTek plastic tanks manufactured out of HDPE sheet, Polypropylene (PP) sheet, Polyvinylchloride (PVC) or other plastics provide long term, corrosion free environment ideal for a diverse range of applications. This incorporates bulk holding purposes to store potable water, chemical, waste and effluent applications...</p>
<div class="btn" style="left:131px;top:2880px;width:108px;height:35px">Read More</div>

<!-- mission -->
<div class="abs mission ph" role="img" aria-label="Welder in protective gear with bright blue sparks"></div>
<div class="abs eyebrow" style="left:610px;top:3072px;color:#ddd">About Us</div>
<div class="abs h" style="left:609px;top:3090px;font:500 34px 'Raleway',sans-serif;color:#fff">Mission Statement</div>
<p class="abs" style="left:610px;top:3151px;width:462px;font-size:12.5px;line-height:20px;color:#e6e6e6">From local outreach to environmental impact, our team is committed to bettering the communities we serve through our processes, practices, and actions</p>
<p class="abs body-sm" style="left:610px;top:3223px;width:465px;color:#cfcfcf">KelbroTek is committed to providing our customers with quality products, on-time and at competitive prices. KelbroTek will treat our employees, suppliers and customers in a fair and equitable manner.</p>
<div class="btn" style="left:609px;top:3308px;width:108px;height:34px">Read More</div>

<!-- contact -->
<div class="abs h" style="left:0;width:1200px;top:3474px;text-align:center;font:500 34px 'Raleway',sans-serif;color:var(--ink)">Contact Us</div>
<div class="abs" style="left:0;width:1200px;top:3523px;text-align:center;font-size:11.5px;color:#333">Have any query? Don't hesitate to communicate with us please send us a SMS or mail.</div>
<div class="abs field" style="left:283px;top:3578px;width:306px;padding-left:12px">First Name:</div>
<div class="abs field" style="left:610px;top:3578px;width:307px;padding-left:12px">Last Name:</div>
<div class="abs field" style="left:283px;top:3626px;width:306px;padding-left:12px">Email:</div>
<div class="abs field" style="left:610px;top:3626px;width:307px;padding-left:12px">Phone:</div>
<div class="abs msg">Message:</div>
<div class="btn" style="left:546px;top:3755px;width:108px;height:35px">Submit</div>

<!-- footer -->
<footer class="abs footer"></footer>
<div class="abs" style="left:131px;top:3915px;color:var(--blue-sky);font:700 40px 'Raleway',sans-serif">KelbroTek</div>
<div class="abs" style="left:143px;top:3984px;font-size:10px;color:#ddd">Design / Engineering / Fabrication</div>
<p class="abs" style="left:131px;top:4024px;width:250px;font-size:10px;line-height:16px;color:#e5e5e5">KelbroTek is committed to providing our customers with quality products, on-time and at competitive prices.</p>
<div class="abs" style="left:131px;top:4100px;display:flex;gap:9px"><span class="soc"></span><span class="soc"></span><span class="soc"></span></div>

<div class="abs f-head" style="left:450px;top:3893px">Quick Links</div>
<div class="abs f-links" style="left:450px;top:3925px">Home<br>About Us<br>Services<br>Our Company<br>Contact Us</div>

<div class="abs f-head" style="left:610px;top:3893px">Cntact Us</div>
<div class="abs" style="left:610px;top:3928px;display:flex;flex-direction:column;gap:16px">
  <div class="f-item"><span class="f-icon"><svg width="10" height="13" viewBox="0 0 24 32"><path d="M12 0C5 0 0 5 0 12c0 9 12 20 12 20s12-11 12-20C24 5 19 0 12 0z" fill="#fff"/><circle cx="12" cy="12" r="4" fill="#1b1b1b"/></svg></span><span>125 Lorem ipsum dolor sit amt<br>Glassglow 25KL USA</span></div>
  <div class="f-item" style="align-items:center"><span class="f-icon"><svg width="11" height="11" viewBox="0 0 24 24"><path fill="#fff" d="M6.6 10.8a15 15 0 0 0 6.6 6.6l2.2-2.2c.3-.3.7-.4 1-.2 1.1.4 2.3.6 3.6.6.6 0 1 .4 1 1V20c0 .6-.4 1-1 1A17 17 0 0 1 3 4c0-.6.4-1 1-1h3.5c.6 0 1 .4 1 1 0 1.3.2 2.5.6 3.6.1.3 0 .7-.2 1z"/></svg></span><span>+2 (555) 407 3921</span></div>
  <div class="f-item" style="align-items:center"><span class="f-icon"><svg width="12" height="9" viewBox="0 0 24 18"><rect width="24" height="18" rx="2" fill="#fff"/><path d="M1 2l11 8 11-8" stroke="#1b1b1b" stroke-width="2" fill="none"/></svg></span><span>info@kelbrotek.com</span></div>
</div>

<div class="abs f-head" style="left:871px;top:3893px">Gallery</div>
<div class="abs" style="left:871px;top:3929px;display:grid;grid-template-columns:repeat(3,64px);gap:3px">
  <div class="gal" style="background:linear-gradient(135deg,#d8c23a,#6b6a5c)" role="img" aria-label="Yellow fabricated parts"></div>
  <div class="gal" style="background:linear-gradient(135deg,#8b8f95,#4d5359)" role="img" aria-label="Workshop machinery"></div>
  <div class="gal" style="background:linear-gradient(135deg,#3a63a8,#8a6a4a)" role="img" aria-label="Steel frames in workshop"></div>
  <div class="gal" style="background:linear-gradient(135deg,#5d6670,#2f353c)" role="img" aria-label="Pipe assembly"></div>
  <div class="gal" style="background:linear-gradient(135deg,#2f62b3,#c9b13a)" role="img" aria-label="Blue and yellow components"></div>
  <div class="gal" style="background:linear-gradient(135deg,#e2c419,#a88e10)" role="img" aria-label="Yellow plastic fittings"></div>
</div>

<div class="abs" style="left:131px;top:4156px;width:939px;height:1px;background:#333"></div>
<div class="abs" style="left:0;width:1200px;top:4183px;text-align:center;font-size:10px;color:#ddd">COPYRIGHT © 2022 <span style="color:var(--blue-sky)">KELBROTEK</span>. ALL RIGHTS RESERVED.</div>

</body>
</html>
```